Letterhead Design Project

Consulting Company , we want a letterhead incorporating both the picture provided and the logo provided. The font name is monotype corsiva.
Target Market(s)
Dentist
Industry/Entity Type
Consulting
Font styles to use
Other font styles liked:
- monotype corsiva

Colors
0455a3
Requirements
Must have
- the logo, the picture (see attached), the website name, the email. and the phone numbers.
- Website: www.tkregulatoryadvisors.solutions
- Email: will be provided to the winner, please use placeholder
- Phone numbers:
- Rhea Lindqvist 5824417093
- Omar Kettering 6148072356

Nice to have
- a swoop or wave across the bottom. a line up the side. I don't know guys. design something unique and professional.

Should not have
- arrows pointing off the logo or anywhere. no arrows. our logo altered in anyway. no broken circles. no variences in blue. we like our logo the way it is. the font is monotype corsiva

```html
<!DOCTYPE html>
<html lang="en">
<head>
<meta charset="utf-8">
<title>TK Regulatory Advisors – Letterhead</title>
<link href="https://fonts.googleapis.com/css2?family=Cormorant+Garamond:ital,wght@1,500&family=Cormorant+Upright:wght@600&family=Noto+Serif&family=Open+Sans&family=Montserrat:wght@400&display=swap" rel="stylesheet">
<style>
  :root{
    --paper:#ffffff;
    --backdrop:#ffffff;
    --sky:#3a9ad9;
    --sky-soft:#bfe0f3;
    --ink-name:#2f4d52;
    --ink-dark:#4a4a4a;
    --ink-body:#8c8c8c;
    --edge:#e2e2e2;
  }
  html,body{margin:0;padding:0;overflow:hidden;background:var(--backdrop);}
  .canvas{width:1200px;height:1120px;overflow:hidden;position:relative;background:var(--backdrop);}
  .stage{width:1240px;height:1160px;position:absolute;left:0;top:0;transform:scale(0.9677);transform-origin:0 0;}
  .sheet{position:absolute;width:630px;height:810px;background:var(--paper);border:1px solid var(--edge);box-sizing:border-box;}
  .sheet--back{left:93px;top:90px;}
  .sheet--front{left:546px;top:288px;}
  .sheet > *{position:absolute;}

  .brand-dot{left:27px;top:31px;width:86px;height:86px;border-radius:50%;background:var(--sky-soft);}
  .brand-lines{left:96px;top:34px;width:266px;}
  .brand-lines span{display:block;height:2px;background:var(--sky);margin-bottom:8px;}
  .brand-lines span:nth-child(1){width:148px;}
  .brand-lines span:nth-child(2){width:203px;margin-left:6px;}
  .brand-lines span:nth-child(3){width:254px;margin-left:12px;}
  .brand-name{left:123px;top:60px;margin:0;font-family:"Cormorant Upright",serif;font-weight:600;font-size:20px;line-height:24px;color:var(--ink-name);white-space:nowrap;}
  .brand-address{left:123px;top:89px;margin:0;font-family:"Cormorant Garamond",serif;font-style:italic;font-weight:500;font-size:12px;line-height:15px;color:var(--ink-dark);white-space:nowrap;}

  .recipient{left:121px;top:164px;margin:0;}
  .recipient .to{font-family:"Noto Serif",serif;font-size:12px;color:var(--ink-body);display:block;}
  .recipient .name{font-family:"Noto Serif",serif;font-size:13px;color:var(--ink-dark);display:block;margin-top:0;}
  .recipient .role{font-family:"Montserrat",sans-serif;font-size:10px;color:var(--ink-dark);display:block;margin-top:6px;line-height:12px;}

  .letter-body{left:124px;top:262px;width:460px;margin:0;font-family:"Open Sans",sans-serif;font-size:10.4px;line-height:14px;color:var(--ink-body);}
  .letter-body p{margin:0 0 14px;}

  .signature{left:130px;top:586px;width:80px;height:24px;background:linear-gradient(90deg,#f4f4f4,#ececec);}
  .signature-rule{left:128px;top:614px;width:82px;height:1px;background:#9a9a9a;}
  .signature-title{left:131px;top:619px;margin:0;font-family:"Montserrat",sans-serif;font-size:8px;letter-spacing:3px;color:var(--ink-dark);}

  .contact{width:180px;text-align:center;top:690px;}
  .contact svg{display:block;margin:0 auto;}
  .contact span{display:block;margin-top:14px;font-family:"Open Sans",sans-serif;font-size:8px;line-height:10px;color:var(--sky);white-space:nowrap;}
  .contact--mail{left:116px;}
  .contact--phone{left:271px;}
  .contact--web{left:426px;}
  .footer-rule{left:120px;top:765px;width:494px;height:1.5px;background:var(--sky);}
</style>
</head>
<body>
<div class="canvas">
 <div class="stage">

  <!-- Blank letterhead sheet -->
  <section class="sheet sheet--back">
    <div class="brand-dot"></div>
    <div class="brand-lines" aria-hidden="true"><span></span><span></span><span></span></div>
    <p class="brand-name">TK Regulatory Advisors, LLC</p>
    <p class="brand-address">418 Larch Hollow Road<br>Ashdale, Kentucky 40912</p>

    <div class="contact contact--mail">
      <svg width="28" height="28" viewBox="0 0 28 28" aria-hidden="true"><circle cx="14" cy="14" r="12" fill="none" stroke="var(--sky)" stroke-width="1.6"/><rect x="8" y="10" width="12" height="8" fill="none" stroke="var(--sky)" stroke-width="1.4"/><polyline points="8,10 14,15 20,10" fill="none" stroke="var(--sky)" stroke-width="1.4"/></svg>
      <span>info@tkregulatoryadvisors.com</span>
    </div>
    <div class="contact contact--phone">
      <svg width="28" height="28" viewBox="0 0 28 28" aria-hidden="true"><circle cx="14" cy="14" r="12" fill="none" stroke="var(--sky)" stroke-width="1.6"/><rect x="10" y="8" width="8" height="12" rx="1" fill="none" stroke="var(--sky)" stroke-width="1.4"/><line x1="12" y1="11" x2="16" y2="11" stroke="var(--sky)" stroke-width="1.2"/><line x1="12" y1="14" x2="16" y2="14" stroke="var(--sky)" stroke-width="1.2"/><line x1="12" y1="17" x2="16" y2="17" stroke="var(--sky)" stroke-width="1.2"/></svg>
      <span>Rhea Lindqvist 5824417093<br>Omar Kettering 6148072356</span>
    </div>
    <div class="footer-rule"></div>
  </section>

  <!-- Filled letterhead sheet -->
  <section class="sheet sheet--front">
    <div class="brand-dot"></div>
    <div class="brand-lines" aria-hidden="true"><span></span><span></span><span></span></div>
    <p class="brand-name">TK Regulatory Advisors, LLC</p>
    <p class="brand-address">418 Larch Hollow Road<br>Ashdale, Kentucky 40912</p>

    <p class="recipient">
      <span class="to">To</span>
      <span class="name">Marcus Ellery</span>
      <span class="role">CEO, NORTHFERN STUDIO<br>M: +91 70215 44836</span>
    </p>

    <div class="letter-body">
      <p>Lorem ipsum dolor sit amet, consectetur adipiscing elit. Pellentesque dictum, ante non ullamcorper convallis, nunc quam blandit metus, ac mollis eros felis a orci. Donec congue, mauris ut pulvinar lobortis, dolor massa feugiat nisi, at tincidunt metus leo vel elit. Proin facilisis semper lobortis. Vivamus augue purus, cursus quis urna non, accumsan pellentesque est. Nulla in iaculis magna, quis aliquet ex. Cras efficitur metus eget purus euismod facilisis. Proin non metus tincidunt, auctor ipsum a, tempor mi. Nulla egestas vulputate risus, ut vestibulum diam commodo id. Mauris ornare libero eu erat porttitor ultrices. Proin sed lectus scelerisque ligula bibendum sagittis ac nec leo. Donec ac accumsan diam, et lobortis mauris.</p>
      <p>Nulla congue volutpat nisl ac lobortis. Integer dignissim interdum libero, quis feugiat velit pretium at. Phasellus sit amet libero rutrum, feugiat odio et, tempus purus. Cras ultricies, leo at fringilla sollicitudin, leo sapien placerat enim, a rutrum lorem enim ut tortor. Phasellus magna ante, congue maximus egestas sit amet, venenatis scelerisque felis.</p>
      <p>Curabitur vitae urna volutpat, varius velit vehicula, fermentum magna. In maximus metus nunc, nec aliquet justo commodo eget. Nullam rhoncus vehicula gravida. Maecenas non sem at erat lacinia convallis. Aliquam at lobortis erat. Etiam rutrum enim metus, vitae molestie tortor tempus eu. Pellentesque non placerat quam, a varius lacus. Maecenas ut lacus ac elit scelerisque volutpat. Proin vitae lectus in felis aliquet gravida vel et nulla.</p>
    </div>

    <div class="signature" role="img" aria-label="Handwritten signature of the director"></div>
    <div class="signature-rule"></div>
    <p class="signature-title">DIRECTOR</p>

    <div class="contact contact--mail">
      <svg width="28" height="28" viewBox="0 0 28 28" aria-hidden="true"><circle cx="14" cy="14" r="12" fill="none" stroke="var(--sky)" stroke-width="1.6"/><rect x="8" y="10" width="12" height="8" fill="none" stroke="var(--sky)" stroke-width="1.4"/><polyline points="8,10 14,15 20,10" fill="none" stroke="var(--sky)" stroke-width="1.4"/></svg>
      <span>info@tkregulatoryadvisors.com</span>
    </div>
    <div class="contact contact--phone">
      <svg width="28" height="28" viewBox="0 0 28 28" aria-hidden="true"><circle cx="14" cy="14" r="12" fill="none" stroke="var(--sky)" stroke-width="1.6"/><rect x="10" y="8" width="8" height="12" rx="1" fill="none" stroke="var(--sky)" stroke-width="1.4"/><line x1="12" y1="11" x2="16" y2="11" stroke="var(--sky)" stroke-width="1.2"/><line x1="12" y1="14" x2="16" y2="14" stroke="var(--sky)" stroke-width="1.2"/><line x1="12" y1="17" x2="16" y2="17" stroke="var(--sky)" stroke-width="1.2"/></svg>
      <span>Rhea Lindqvist 5824417093<br>Omar Kettering 6148072356</span>
    </div>
    <div class="contact contact--web">
      <svg width="28" height="28" viewBox="0 0 28 28" aria-hidden="true"><circle cx="14" cy="14" r="12" fill="none" stroke="var(--sky)" stroke-width="1.6"/><circle cx="14" cy="14" r="6" fill="none" stroke="var(--sky)" stroke-width="1.4"/><ellipse cx="14" cy="14" rx="2.6" ry="6" fill="none" stroke="var(--sky)" stroke-width="1.2"/><line x1="8" y1="14" x2="20" y2="14" stroke="var(--sky)" stroke-width="1.2"/></svg>
      <span>www.tkregulatoryadvisors.solutions</span>
    </div>
    <div class="footer-rule"></div>
  </section>

 </div>
</div>
</body>
</html>
```